Webdesign für Entwickler von Immobilienprojekten in Mallorca
Zielgruppe
Wir entwickeln Immobilienprojekte in Mallorca, überwiegend in den schönen direkt am Meer gelegenen Orten Portixol und Molinar, die Stadtteile von Palma sind. Aber auch im ländlichen Bereich, z.B. in Pollenca.
Unser Ansatz ist durch meine Historie als rechnerguenstig.de Gründer etwas 'Anders'. Ich versuche, das Bauträger Geschäft ähnlich transparent und modern wie ein Online-Handels-Unternehmen zu gestalten. Wir bauen wesentlich hochwertiger als die meisten Bauträger. Versuchen aber, sehr faire Preise darzustellen, obwohl wir hier durch die Lagen im Preisbereich eher zwischen 1 und 4 Millionen unterwegs sind.
Ich wünsche mir ein modernes schlichtes Design, das aber viel Raum für Persönlichkeit hat. Bisher arbeite ich mit wix. Finde das auch gar nicht so schlecht. Und habe aktuell nur einen One Pager für das Projekt VelaroHofhaeuser auf der Seite kestrivo.com
Die zukünftige Struktur der Seite stelle ich mir etwa wie folgt vor:
Home
Projects
- Velaro Hofhaeuser
- Brisada Landgut
- Saliner trifft Toskana
Team
- generell Info über uns
- Kurzportrait der Team Members und auch einzelner Externer (3-5 Leute)
Blog (können wir den von Wix ruhig weiter verwenden denke ich)
Für mich wäre es super, wenn wir bei wix bleiben könnten. Oder ich ein vergleichbar einfaches Tool habe, um selber am Content zu basteln. Es ist für mich super relevant, das ich laufend Dinge ändern und aktualisieren kann und das wir auf Google mehr Relevanz kriegen. Auch eine möglichst 'befruchtende' Verknüpfung zwischen instagram, facebook, blog und seite wäre super!
Aufgabenstellung
Farben gerne mediterran. Gerne pastelltöne blau, grün, türkis. Das Logo der Kestrivo ist in orange. Und die Kombination böte bei geschickter Umsetzung gute Möglichkeiten, zwischen verschiedenen Content Arten zu differenzieren. Im Zweifel kann aber auch nur das Logo orange sein, wenn Ihr das besser findet.
Bildmaterial habe ich noch nicht Alles. Ich lasse gerade noch paar Sachen fotografieren. Ich habe Euch aber schon mal paar Bilder, die Ihr verwenden könnt (alle VelaroHofhaus) beigefügt. Für die anderen

```html
<!DOCTYPE html>
<html lang="en">
<head>
<meta charset="utf-8">
<title>Kestrivo SL – Real Estate Projects in Mallorca</title>
<link href="https://fonts.googleapis.com/css2?family=Lato:ital,wght@0,300;0,400;0,700;0,900;1,700;1,900&display=swap" rel="stylesheet">
<style>
:root{
  --orange:#f26a1b;
  --orange-soft:#f08a4b;
  --slate:#6b7e8d;
  --slate-light:#8795a2;
  --slate-dark:#6c7c89;
  --heading:#6d7c88;
  --text:#6a6a6a;
  --ink:#333;
  --grey-bg:#f2f2f2;
  --white:#fff;
}
*{margin:0;padding:0;box-sizing:border-box}
html,body{width:1200px;height:2882px;overflow:hidden;background:var(--white)}
body{position:relative;font-family:'Lato',sans-serif;color:var(--text)}
.abs{position:absolute}

.topline{left:0;top:0;width:1200px;height:3px;background:var(--orange)}
.brand{top:14px;left:0;width:1200px;display:flex;justify-content:center;align-items:center;gap:12px}
.brand-dot{width:34px;height:34px;border-radius:50%;background:var(--orange)}
.brand-name{font-size:29px;font-weight:400;letter-spacing:5px;color:var(--orange)}

.nav{left:0;top:67px;width:1200px;height:44px;background:var(--slate)}
.nav a{position:absolute;top:0;height:44px;line-height:44px;font-size:13px;font-weight:700;color:var(--white);text-decoration:none;letter-spacing:.5px;text-align:center}
.nav a.active{background:var(--orange)}

.hero-photo{left:0;top:111px;width:1200px;height:520px;background:linear-gradient(135deg,#e9dfd2 0%,#d8c3a6 35%,#8f7a63 60%,#cfc6bb 100%)}
.hero-curve{left:0;top:111px}
.hero-arrow{width:56px;height:56px;border-radius:50%;background:var(--orange);top:287px}
.hero-badge{left:560px;top:495px;width:80px;height:80px;border-radius:50%;background:var(--white);border:5px solid var(--orange)}
.hero-badge span{position:absolute;left:17px;top:17px;width:36px;height:36px;border-radius:50%;background:var(--orange)}

.intro-title{left:150px;top:711px;color:var(--heading);font-weight:900;line-height:1}
.intro-title .l1{font-size:27px;font-weight:700}
.intro-title .l2{font-size:42px;margin-top:2px}
.intro-title .l3{font-size:56px}
.intro-title .l4{font-size:27px;color:var(--orange);font-weight:700;margin-top:4px}
.intro-text{left:444px;top:710px;width:616px;font-size:14px;line-height:22.5px;font-weight:300;color:#555;text-align:justify}
.intro-text p{margin-bottom:22.5px}
.intro-text b{font-weight:700;color:#333}

.projects-band{left:0;top:1000px;width:1200px;height:560px;background:var(--grey-bg)}
.section-title{left:0;width:1200px;text-align:center;font-size:29px;font-weight:900;color:var(--orange)}
.section-sub{left:0;width:1200px;text-align:center;font-size:14px;color:#555}
.project-card{top:1207px;width:281px}
.project-photo{width:281px;height:208px}
.project-name{text-align:center;font-size:18px;font-weight:700;color:var(--orange);margin-top:8px;line-height:1}
.project-type{text-align:center;font-size:14px;font-weight:700;color:#8a8a8a;line-height:1.2}
.search-dot{left:116px;top:76px;width:42px;height:42px;border-radius:50%;background:var(--orange)}

.member{top:1682px;width:208px}
.member-photo{width:208px;height:264px;border-bottom:3px solid var(--orange)}
.member-name{text-align:center;font-size:16px;font-style:italic;font-weight:900;color:var(--orange);margin-top:8px}
.member-role{text-align:center;font-size:14px;color:#777;margin-top:3px}

.blog-band{left:0;top:2116px;width:1200px;height:537px;background:linear-gradient(160deg,#f08a48 0%,#ef7a33 50%,#f28f52 100%)}
.blog-card{top:2270px;width:281px;height:327px;background:var(--white);border-radius:4px;overflow:hidden}
.blog-photo{width:281px;height:170px}
.blog-body{padding:14px 18px 0 19px}
.blog-heading{font-size:17px;font-weight:900;color:var(--orange)}
.blog-text{font-size:12.5px;line-height:15px;color:var(--ink);margin-top:12px;padding-left:2px}
.read-more{display:flex;align-items:center;gap:9px;font-size:13px;color:var(--ink);margin-top:12px;padding-left:2px}

.footer{left:0;top:2653px;width:1200px;height:185px;background:var(--slate-light)}
.footer-bottom{left:0;top:2838px;width:1200px;height:44px;background:var(--slate-dark);color:var(--white);font-size:13px;text-align:center;line-height:44px}
.footer-brand{left:205px;top:2690px;width:185px;display:flex;flex-direction:column;align-items:center;gap:14px}
.footer-dot{width:60px;height:60px;border-radius:50%;background:var(--white)}
.footer-name{font-size:23px;letter-spacing:4px;color:var(--white);font-weight:400}
.footer-address{left:498px;top:2697px;font-size:14.5px;line-height:24px;color:var(--white)}
.footer-mail{left:498px;top:2770px;font-size:14.5px;color:var(--white);display:flex;align-items:center;gap:11px}
.social{top:2690px;width:40px;height:40px;border-radius:50%;border:3px solid var(--white)}
</style>
</head>
<body>

<header>
  <div class="abs topline"></div>
  <div class="abs brand"><span class="brand-dot"></span><span class="brand-name">KESTRIVO SL</span></div>
  <nav class="abs nav">
    <a class="active" href="#" style="left:299px;width:112px">HOME</a>
    <a href="#" style="left:438px;width:80px">PROJECTS</a>
    <a href="#" style="left:578px;width:60px">TEAM</a>
    <a href="#" style="left:686px;width:60px">BLOG</a>
    <a href="#" style="left:792px;width:80px">CONTACT</a>
  </nav>
</header>

<section class="hero">
  <div class="abs hero-photo" role="img" aria-label="Photo of a bright open-plan living and dining room with kitchen"></div>
  <svg class="abs hero-curve" width="1200" height="520" viewBox="0 0 1200 520">
    <path d="M0 518 C250 452 450 425 600 424 C800 423 1000 440 1200 460 L1200 520 L0 520 Z" fill="#fff"/>
    <path d="M260 462 C420 432 510 425 600 424 C800 423 1000 440 1200 462" fill="none" stroke="#f26a1b" stroke-width="6"/>
  </svg>
  <div class="abs hero-arrow" style="left:150px">
    <svg width="56" height="56" viewBox="0 0 56 56"><path d="M31 20 L23 28 L31 36" fill="none" stroke="#fff" stroke-width="2"/></svg>
  </div>
  <div class="abs hero-arrow" style="left:993px">
    <svg width="56" height="56" viewBox="0 0 56 56"><path d="M25 20 L33 28 L25 36" fill="none" stroke="#fff" stroke-width="2"/></svg>
  </div>
  <div class="abs hero-badge"><span></span></div>
</section>

<section class="intro">
  <h1 class="abs intro-title">
    <div class="l1">WE DEVELOP</div>
    <div class="l2">REAL ESTATE</div>
    <div class="l3">PROJECTS</div>
    <div class="l4">IN MALLORCA</div>
  </h1>
  <div class="abs intro-text">
    <p>Welcome on our website! Kestrivo SL develops high end real estate projects in Mallorca, especially in Palmas nicest areas of Portixol and Molinar. We also develop finca projects in Pollenca, you will find more details soon! Our building quality is at a superb standard and we work with a very close and fixed team of professionals to achieve a constant quality that will make you enjoy your new real estate for a very long time.</p>
    <p>We sell and rent. Depending on the project. Our <b>sales projects</b> you find on this website.</p>
    <p>The rental part is located at <b>salinerhomes.com</b>.</p>
  </div>
</section>

<section class="projects">
  <div class="abs projects-band"></div>
  <svg class="abs" style="left:0;top:1000px" width="1200" height="60" viewBox="0 0 1200 60">
    <path d="M0 8 C300 52 520 58 760 44 C950 33 1100 22 1200 18 L1200 0 L0 0 Z" fill="#fff"/>
    <path d="M0 8 C300 52 520 58 760 44" fill="none" stroke="#f26a1b" stroke-width="5"/>
  </svg>
  <h2 class="abs section-title" style="top:1116px">OUR PROJECTS</h2>
  <p class="abs section-sub" style="top:1152px">Check our recent projects</p>

  <svg class="abs" style="left:80px;top:1347px" width="26" height="40" viewBox="0 0 26 40"><path d="M20 2 L4 20 L20 38" fill="none" stroke="#555" stroke-width="2"/></svg>
  <svg class="abs" style="left:1094px;top:1347px" width="26" height="40" viewBox="0 0 26 40"><path d="M6 2 L22 20 L6 38" fill="none" stroke="#555" stroke-width="2"/></svg>

  <div class="abs project-card" style="left:150px">
    <div class="project-photo" role="img" aria-label="Photo of a dining area with green chairs and a sofa" style="background:linear-gradient(135deg,#f3e9dc,#d9c4a4 55%,#b8a890)"></div>
    <div class="project-name">VELARO</div>
    <div class="project-type">Hofhaus</div>
  </div>
  <div class="abs project-card" style="left:460px">
    <div class="project-photo" role="img" aria-label="Photo of a bathroom with patterned tiles and a wash basin" style="position:relative;background:linear-gradient(135deg,#d8b79c,#e9d2c0 50%,#c9a889)">
      <div class="abs search-dot">
        <svg width="42" height="42" viewBox="0 0 42 42"><circle cx="18" cy="18" r="7" fill="none" stroke="#fff" stroke-width="3"/><path d="M23 23 L31 31" stroke="#fff" stroke-width="4" stroke-linecap="round"/></svg>
      </div>
    </div>
    <div class="project-name">BRISADA</div>
    <div class="project-type">Landgut</div>
  </div>
  <div class="abs project-card" style="left:767px">
    <div class="project-photo" role="img" aria-label="Photo of a dining table with dark chairs next to the kitchen" style="background:linear-gradient(135deg,#e6dccd,#b79a78 50%,#d8d0c5)"></div>
    <div class="project-name">BRISADA</div>
    <div class="project-type">Landgut</div>
  </div>

  <svg class="abs" style="left:0;top:1500px" width="1200" height="62" viewBox="0 0 1200 62">
    <path d="M0 47 C300 28 600 8 850 12 C1000 15 1120 30 1200 50 L1200 62 L0 62 Z" fill="#fff"/>
    <path d="M600 10 C800 8 1000 14 1200 52" fill="none" stroke="#f26a1b" stroke-width="6"/>
  </svg>
</section>

<section class="team">
  <h2 class="abs section-title" style="top:1629px">OUR TEAM</h2>
  <svg class="abs" style="left:86px;top:1795px" width="30" height="48" viewBox="0 0 30 48"><path d="M26 2 L4 24 L26 46" fill="none" stroke="#6d7c88" stroke-width="3"/></svg>
  <svg class="abs" style="left:1085px;top:1795px" width="30" height="48" viewBox="0 0 30 48"><path d="M4 2 L26 24 L4 46" fill="none" stroke="#6d7c88" stroke-width="3"/></svg>

  <div class="abs member" style="left:150px">
    <div class="member-photo" role="img" aria-label="Portrait photo of a team member in a dark suit" style="background:linear-gradient(180deg,#dde3e8,#3c4450)"></div>
    <div class="member-name">RAMON VIDAL</div>
    <div class="member-role">Position here</div>
  </div>
  <div class="abs member" style="left:382px">
    <div class="member-photo" role="img" aria-label="Portrait photo of a team member in a light blue shirt" style="background:linear-gradient(180deg,#3f4044,#9ab3cc)"></div>
    <div class="member-name">RAMON VIDAL</div>
    <div class="member-role">Position here</div>
  </div>
  <div class="abs member" style="left:611px">
    <div class="member-photo" role="img" aria-label="Portrait photo of a team member in a navy blazer" style="background:linear-gradient(180deg,#e4e8ec,#2d3548)"></div>
    <div class="member-name">LUCIA FERRER</div>
    <div class="member-role">Position here</div>
  </div>
  <div class="abs member" style="left:842px">
    <div class="member-photo" role="img" aria-label="Portrait photo of a team member in a light blue shirt" style="background:linear-gradient(180deg,#3f4044,#9ab3cc)"></div>
    <div class="member-name">RAMON VIDAL</div>
    <div class="member-role">Position here</div>
  </div>
</section>

<section class="blog">
  <div class="abs blog-band" role="img" aria-label="Orange tinted photo of an interior as section background"></div>
  <svg class="abs" style="left:0;top:2105px" width="1200" height="60" viewBox="0 0 1200 60">
    <path d="M0 48 C300 30 600 10 880 8 C1030 7 1130 16 1200 30 L1200 0 L0 0 Z" fill="#fff"/>
    <path d="M600 12 C800 4 1050 5 1200 34" fill="none" stroke="#7b8b98" stroke-width="6"/>
  </svg>
  <h2 class="abs section-title" style="top:2205px;color:#fff">RECENT BLOG POSTS</h2>

  <article class="abs blog-card" style="left:150px">
    <div class="blog-photo" role="img" aria-label="Photo of a dining area with a modern kitchen" style="background:linear-gradient(135deg,#eee6da,#9d8b76 55%,#d5ccc0)"></div>
    <div class="blog-body">
      <h3 class="blog-heading">HEADING GOES HERE</h3>
      <p class="blog-text">Lorem ipsum dolor sit amet, consectetur adipiscing elit, sed do eiusmod tempor incididunt ut labore et dolore magna aliqua.</p>
      <div class="read-more"><svg width="14" height="10" viewBox="0 0 14 10"><path d="M0 5 H12 M8 1 L12 5 L8 9" fill="none" stroke="#333" stroke-width="1.6"/></svg>Read More</div>
    </div>
  </article>
  <article class="abs blog-card" style="left:460px">
    <div class="blog-photo" role="img" aria-label="Photo of a courtyard with a pool and wooden deck" style="background:linear-gradient(180deg,#e9ebe6,#c7b9a4 60%,#6fa3b8)"></div>
    <div class="blog-body">
      <h3 class="blog-heading">HEADING GOES HERE</h3>
      <p class="blog-text">Lorem ipsum dolor sit amet, consectetur adipiscing elit, sed do eiusmod tempor incididunt ut labore et dolore magna aliqua.</p>
      <div class="read-more"><svg width="14" height="10" viewBox="0 0 14 10"><path d="M0 5 H12 M8 1 L12 5 L8 9" fill="none" stroke="#333" stroke-width="1.6"/></svg>Read More</div>
    </div>
  </article>
  <article class="abs blog-card" style="left:770px">
    <div class="blog-photo" role="img" aria-label="Photo of a modern house terrace at dusk" style="background:linear-gradient(180deg,#4f6178,#7a6a58 60%,#3a3936)"></div>
    <div class="blog-body">
      <h3 class="blog-heading">HEADING GOES HERE</h3>
      <p class="blog-text">Lorem ipsum dolor sit amet, consectetur adipiscing elit, sed do eiusmod tempor incididunt ut labore et dolore magna aliqua.</p>
      <div class="read-more"><svg width="14" height="10" viewBox="0 0 14 10"><path d="M0 5 H12 M8 1 L12 5 L8 9" fill="none" stroke="#333" stroke-width="1.6"/></svg>Read More</div>
    </div>
  </article>
</section>

<footer>
  <div class="abs footer"></div>
  <div class="abs footer-brand"><span class="footer-dot"></span><span class="footer-name">KESTRIVO SL</span></div>
  <address class="abs footer-address" style="font-style:normal">Calle Marina Baixa, 14<br>07006 Palma de Mallorca - Portixol</address>
  <div class="abs footer-mail">
    <svg width="17" height="12" viewBox="0 0 17 12"><rect x="0.7" y="0.7" width="15.6" height="10.6" fill="none" stroke="#fff" stroke-width="1.4"/><path d="M1 1 L8.5 7 L16 1" fill="none" stroke="#fff" stroke-width="1.4"/></svg>
    info@kestrivo.com
  </div>
  <div class="abs social" style="left:939px" role="img" aria-label="Social network link"></div>
  <div class="abs social" style="left:1010px" role="img" aria-label="Photo sharing network link"></div>
  <div class="abs footer-bottom">© 2020 Kestrivo S.L. Numéro de Intentificacion Fiscal B41827306</div>
</footer>

</body>
</html>
```